Mediation Website Design Upgrade

Project Details: https://files.brellowin.net/sheet/v/8kPw3xTzLmQa7NbYr2HdVcEuFj_9Gs-41kh5XoWe/view?mode=public

Number of Pages Required

2 page

Font styles to use
Sans Serif

```html
<!DOCTYPE html>
<html lang="en">
<head>
<meta charset="utf-8">
<title>Harbor Mediation Group – Our Services</title>
<link href="https://fonts.googleapis.com/css2?family=Rubik:wght@400;500&display=swap" rel="stylesheet">
<style>
:root{
  --teal:#5b8983;
  --teal-dark:#497a74;
  --teal-light:#6e9d97;
  --mist:#e1e9e8;
  --panel:#f7f8f7;
  --ink:#2b2b2b;
  --muted:#9aa9a7;
  --olive:#7a9a2e;
  --white:#ffffff;
}
*{margin:0;padding:0;box-sizing:border-box}
html,body{width:1200px;height:2389px;overflow:hidden;background:var(--white);font-family:'Rubik',sans-serif;color:var(--ink)}
.page{position:relative;width:1200px;height:2389px}
.abs{position:absolute}
.caps{text-transform:uppercase;font-weight:500}

/* header */
.brand{left:253px;top:40px;display:flex;align-items:center;gap:8px;font-size:12px;font-weight:500;color:var(--ink)}
.brand-dot{width:20px;height:20px;border-radius:50%;background:var(--teal)}
.callback{left:454px;top:38px;display:flex;gap:18px;align-items:center}
.callback small{display:block;font-size:7px;letter-spacing:1px;color:var(--muted);text-transform:uppercase}
.callback strong{font-size:14px;font-weight:500}
.top-links{top:52px;font-size:8.5px}
.top-links a{position:absolute;color:var(--ink);text-decoration:none;white-space:nowrap}
.top-links .active{color:var(--olive)}
.top-underline{left:826px;top:72px;width:65px;height:2px;background:var(--olive)}

.seam{left:0;top:109px;width:1200px;height:6px;background:var(--mist)}
.mainnav{left:0;top:115px;width:1200px;height:79px;background:var(--teal);color:var(--white);font-size:9.5px}
.mainnav .item{position:absolute;top:34px;white-space:nowrap}
.mainnav .current{left:400px;top:0;width:190px;height:79px;background:var(--teal-dark)}

.titleband{left:0;top:194px;width:1200px;height:118px;background:var(--mist)}
.titleband h1{position:absolute;left:288px;top:40px;font-size:19px;font-weight:500}
.titleband p{position:absolute;left:288px;top:68px;font-size:8.5px;letter-spacing:1.5px;color:var(--teal);font-weight:500}

/* sidebar */
.side{left:253px;width:219px;background:var(--panel)}
.side h3{position:absolute;left:23px;font-size:9px;font-weight:500}
.side .rule{position:absolute;left:23px;width:174px;height:1px;background:#e2e6e5}
.svc{position:absolute;left:36px;font-size:9px;font-weight:500;line-height:11.5px;text-transform:uppercase}
.svc-active{position:absolute;left:21px;width:176px;height:41px;background:var(--teal)}
.phonebox{position:absolute;left:19px;top:66px;width:180px;height:55px;background:#eef1f0}
.phonebox strong{position:absolute;left:52px;top:14px;font-size:13.5px;font-weight:500}
.phonebox small{position:absolute;left:52px;top:34px;font-size:6.5px;letter-spacing:1px;color:#b3bdbb}
.side .note{position:absolute;left:21px;top:147px;width:180px;font-size:8px;line-height:14.4px}
.outline-btn{position:absolute;left:23px;top:213px;width:175px;height:34px;border:1px solid var(--olive);color:var(--olive);font-size:8.5px;letter-spacing:1.5px;display:flex;align-items:center;justify-content:center;font-weight:500}
.social{position:absolute;top:13px;width:36px;height:36px;border-radius:50%;background:#4a4a4a;color:var(--white);font-size:7px;display:flex;align-items:center;justify-content:center}
.social.on{background:var(--teal)}

/* main */
.main{left:490px;width:456px}
.heading{top:368px;font-size:18.5px;font-weight:500}
.heading-rule{left:491px;top:398px;width:91px;height:4px;background:var(--mist)}
.copy p{position:absolute;left:1px;width:456px;font-size:9.6px;line-height:16.2px}
.box{left:490px;width:456px;background:var(--panel)}
.box h4{position:absolute;left:30px;width:380px;font-size:9px;font-weight:500;color:var(--teal);line-height:15px;text-transform:uppercase}
.tick{position:absolute;left:40px;width:10px;height:8px}
.li{position:absolute;left:64px;width:360px;font-size:9.6px;line-height:16.2px}
.dash{position:absolute;left:64px;width:300px;border-top:1px dashed #dfe4e3}
.hl{position:absolute;left:0;width:456px;height:49px;background:#edf1f0}

.cta{left:490px;top:1569px;width:456px;height:134px;background:var(--teal);color:var(--white)}
.cta .stripe{position:absolute;left:0;top:0;width:11px;height:134px;background:var(--teal-light)}
.cta p{position:absolute;left:113px;top:24px;width:310px;font-size:9.6px;line-height:16.2px}
.cta .btn{position:absolute;left:113px;top:78px;width:230px;height:33px;border:1px solid var(--white);font-size:8.5px;letter-spacing:1.5px;display:flex;align-items:center;justify-content:center;font-weight:500}

/* footer */
.foot-seam{left:0;top:1769px;width:1200px;height:18px;background:var(--mist)}
.footer{left:0;top:1787px;width:1200px;height:239px;background:var(--teal);color:var(--white)}
.footer .col{position:absolute;top:44px}
.footer h5{font-size:8.5px;font-weight:500;text-transform:uppercase;white-space:nowrap}
.footer .bar{width:36px;height:2px;background:var(--teal-light);margin-top:6px}
.footer ul{list-style:none;font-size:8.5px}
.footer .primary li{font-weight:500;text-transform:uppercase;height:22.5px}
.footer .links{margin-top:15px}
.footer .links li{height:23.5px}
.copyright{left:0;top:2026px;width:1200px;height:40px;background:var(--teal-light);color:#cde0dc;font-size:8px;display:flex;align-items:center;justify-content:center}
</style>
</head>
<body>
<div class="page">

  <header>
    <div class="abs brand"><span class="brand-dot"></span>Harbor Mediation Group</div>
    <div class="abs callback">
      <svg width="18" height="18" viewBox="0 0 24 24" fill="#333"><path d="M6.6 10.8a15 15 0 0 0 6.6 6.6l2.2-2.2a1 1 0 0 1 1-.25 11.4 11.4 0 0 0 3.6.57 1 1 0 0 1 1 1V20a1 1 0 0 1-1 1A17 17 0 0 1 3 4a1 1 0 0 1 1-1h3.5a1 1 0 0 1 1 1c0 1.25.2 2.45.57 3.57a1 1 0 0 1-.25 1z"/></svg>
      <div><small>We will call you back</small><strong>555 - 014 - 2290</strong></div>
    </div>
    <nav class="abs top-links caps">
      <a style="left:784px">Blog</a>
      <a class="active" style="left:835px">About us</a>
      <a style="left:907px">Contact</a>
    </nav>
    <div class="abs top-underline"></div>
  </header>

  <div class="abs seam"></div>
  <nav class="abs mainnav caps">
    <div class="abs current"></div>
    <span class="item" style="left:336px">Home</span>
    <span class="item" style="left:435px">Meditation services
      <svg width="8" height="6" style="margin-left:9px" viewBox="0 0 8 6"><path d="M0 0h8L4 5z" fill="#fff"/></svg></span>
    <span class="item" style="left:634px">Conflict consulting</span>
    <span class="item" style="left:814px">Negotiation</span>
  </nav>

  <section class="abs titleband">
    <svg class="abs" style="left:255px;top:54px" width="18" height="18" viewBox="0 0 24 24" fill="none" stroke="#555" stroke-width="1.6"><path d="M10 14a4 4 0 0 1 0-5.6l3-3a4 4 0 0 1 5.6 5.6l-1.5 1.5M14 10a4 4 0 0 1 0 5.6l-3 3a4 4 0 0 1-5.6-5.6l1.5-1.5"/></svg>
    <h1>Our Services</h1>
    <p class="caps">Your sub-headline here</p>
  </section>

  <!-- services sidebar -->
  <aside class="abs side" style="top:341px;height:392px">
    <h3 class="caps" style="top:24px">Services</h3>
    <div class="rule" style="top:48px"></div>
    <span class="svc" style="top:80px">Commercial mediation</span>
    <div class="svc-active" style="top:114px"></div>
    <span class="svc" style="top:130px;color:#fff">Conflict coaching</span>
    <span class="svc" style="top:176px">Family mediation</span>
    <span class="svc" style="top:220px">Meeting or project<br>facilitation</span>
    <span class="svc" style="top:277px">Negotiation</span>
    <span class="svc" style="top:322px">Divorce &amp; post-divorce<br>mediation</span>
  </aside>

  <aside class="abs side" style="top:772px;height:271px">
    <h3 class="caps" style="top:24px">Free initial consultation</h3>
    <div class="rule" style="top:49px"></div>
    <div class="phonebox">
      <svg class="abs" style="left:14px;top:16px" width="22" height="22" viewBox="0 0 24 24" fill="#333"><path d="M6.6 10.8a15 15 0 0 0 6.6 6.6l2.2-2.2a1 1 0 0 1 1-.25 11.4 11.4 0 0 0 3.6.57 1 1 0 0 1 1 1V20a1 1 0 0 1-1 1A17 17 0 0 1 3 4a1 1 0 0 1 1-1h3.5a1 1 0 0 1 1 1c0 1.25.2 2.45.57 3.57a1 1 0 0 1-.25 1z"/></svg>
      <strong>555 - 014 - 2290</strong><small>WE WILL CALL YOU BACK</small>
    </div>
    <p class="note">Click the button below to detail the best way to contact you here and Clara will call or email you to arrange a no cost informational session.</p>
    <div class="outline-btn">CONTACT US</div>
  </aside>

  <aside class="abs side" style="top:1083px;height:64px">
    <span class="social" style="left:40px">Forum</span>
    <span class="social on" style="left:91px">Feed</span>
    <span class="social" style="left:142px">Network</span>
  </aside>

  <!-- main content -->
  <h2 class="abs main heading">Mediation Services – Our Primary Focus</h2>
  <div class="abs heading-rule"></div>
  <div class="abs main copy" style="top:0">
    <p style="top:433px"><strong style="font-weight:500">HMG</strong> offers decades of conflict resolution experience in such diverse settings as community meetings, non-profit boards, courts, corporate boardrooms, family living rooms and kitchen tables.</p>
    <p style="top:498px">Firm principal Clara Whitfield has worked for <strong style="font-weight:500">over 30 years</strong> in various business, family and organizational settings including finance, insurance, technology, restaurants, family businesses and many nonprofits. These nonprofits include community foundations, higher education, art cooperatives and religious communities.</p>
    <p style="top:580px">In addition to formal training and business experience, Clara’s life has uniquely prepared her for a career in mediation. She grew up in a large extended family, is now part of a blended family, and has worked through inter-generational and family business issues throughout her life.</p>
    <p style="top:645px">Based on Clara’s experience, education, and passion, her firm specializes in selected area of the growing conflict resolution field.</p>
  </div>

  <section class="abs box" style="top:705px;height:292px">
    <h4 style="top:21px">Key areas of focus include</h4>
    <div class="hl" style="top:118px"></div>
    <svg class="tick" style="top:62px" viewBox="0 0 10 8"><path d="M1 4l3 3 5-6" stroke="#5b8983" stroke-width="1.4" fill="none"/></svg>
    <span class="li" style="top:60px">Conflict Coaching</span>
    <div class="dash" style="top:84px"></div>
    <svg class="tick" style="top:96px" viewBox="0 0 10 8"><path d="M1 4l3 3 5-6" stroke="#5b8983" stroke-width="1.4" fill="none"/></svg>
    <span class="li" style="top:94px">Adult-Sibling and Elder Mediation</span>
    <svg class="tick" style="top:130px" viewBox="0 0 10 8"><path d="M1 4l3 3 5-6" stroke="#5b8983" stroke-width="1.4" fill="none"/></svg>
    <span class="li" style="top:128px">Commercial Mediation – within the same organization or between different organizations</span>
    <svg class="tick" style="top:178px" viewBox="0 0 10 8"><path d="M1 4l3 3 5-6" stroke="#5b8983" stroke-width="1.4" fill="none"/></svg>
    <span class="li" style="top:176px">Nonprofit Mediation</span>
    <div class="dash" style="top:200px"></div>
    <svg class="tick" style="top:212px" viewBox="0 0 10 8"><path d="M1 4l3 3 5-6" stroke="#5b8983" stroke-width="1.4" fill="none"/></svg>
    <span class="li" style="top:210px">Facilitation of meetings and processes</span>
    <div class="dash" style="top:234px"></div>
    <svg class="tick" style="top:246px" viewBox="0 0 10 8"><path d="M1 4l3 3 5-6" stroke="#5b8983" stroke-width="1.4" fill="none"/></svg>
    <span class="li" style="top:244px">Negotiation – coaching or as an agent</span>
  </section>

  <section class="abs box" style="top:1028px;height:425px">
    <h4 style="top:22px">Working with a professional, mediation can perform any of the following tasks and more:</h4>
    <svg class="tick" style="top:80px" viewBox="0 0 10 8"><path d="M1 4l3 3 5-6" stroke="#5b8983" stroke-width="1.4" fill="none"/></svg>
    <span class="li" style="top:79px">Organize discussions for thorough and timely consideration</span>
    <div class="dash" style="top:103px"></div>
    <svg class="tick" style="top:114px" viewBox="0 0 10 8"><path d="M1 4l3 3 5-6" stroke="#5b8983" stroke-width="1.4" fill="none"/></svg>
    <span class="li" style="top:113px">Work to provide safe discussions while promoting candidness and honesty</span>
    <div class="dash" style="top:137px"></div>
    <svg class="tick" style="top:148px" viewBox="0 0 10 8"><path d="M1 4l3 3 5-6" stroke="#5b8983" stroke-width="1.4" fill="none"/></svg>
    <span class="li" style="top:147px">Enlist objective subject matter experts to ensure that pertinent and accurate information is available for decision making</span>
    <div class="dash" style="top:186px"></div>
    <svg class="tick" style="top:196px" viewBox="0 0 10 8"><path d="M1 4l3 3 5-6" stroke="#5b8983" stroke-width="1.4" fill="none"/></svg>
    <span class="li" style="top:195px">Ensure that all viewpoints and perspectives are heard and considered</span>
    <div class="dash" style="top:219px"></div>
    <svg class="tick" style="top:230px" viewBox="0 0 10 8"><path d="M1 4l3 3 5-6" stroke="#5b8983" stroke-width="1.4" fill="none"/></svg>
    <span class="li" style="top:229px">Develop a process by which the situation is explored and viable alternatives are identified</span>
    <div class="dash" style="top:268px"></div>
    <svg class="tick" style="top:279px" viewBox="0 0 10 8"><path d="M1 4l3 3 5-6" stroke="#5b8983" stroke-width="1.4" fill="none"/></svg>
    <span class="li" style="top:278px">Establish criteria by which forward progress occurs</span>
    <div class="dash" style="top:302px"></div>
    <svg class="tick" style="top:312px" viewBox="0 0 10 8"><path d="M1 4l3 3 5-6" stroke="#5b8983" stroke-width="1.4" fill="none"/></svg>
    <span class="li" style="top:311px">Oversee delicate or difficult decision making</span>
    <div class="dash" style="top:335px"></div>
    <svg class="tick" style="top:346px" viewBox="0 0 10 8"><path d="M1 4l3 3 5-6" stroke="#5b8983" stroke-width="1.4" fill="none"/></svg>
    <span class="li" style="top:345px">Document outcomes, plans, and responsibilities</span>
    <div class="dash" style="top:369px"></div>
    <svg class="tick" style="top:380px" viewBox="0 0 10 8"><path d="M1 4l3 3 5-6" stroke="#5b8983" stroke-width="1.4" fill="none"/></svg>
    <span class="li" style="top:379px">Provide counsel and guidance for implementing new plans</span>
  </section>

  <div class="abs main copy" style="top:0">
    <p style="top:1496px">Whether for your business, nonprofit organization or family and personal issues, you can explore mutually satisfying solutions through our caring and professional mediation practice.</p>
  </div>

  <section class="abs cta">
    <div class="stripe"></div>
    <svg class="abs" style="left:44px;top:51px" width="34" height="32" viewBox="0 0 34 32" fill="none" stroke="#fff" stroke-width="1.3"><rect x="1" y="4" width="28" height="24"/><path d="M1 10h28M7 1v6M23 1v6"/><circle cx="25" cy="24" r="6" fill="#5b8983"/><path d="M25 21v3h2"/></svg>
    <p>Learn how mediation can help you quickly and confidently move on to the next chapter of your life.</p>
    <div class="btn">SCHEDULE YOUR CONSULTATION</div>
  </section>

  <!-- footer -->
  <div class="abs foot-seam"></div>
  <footer class="abs footer">
    <div class="col" style="left:253px">
      <ul class="primary"><li>Home</li><li>About us</li><li>Our services</li><li>Blog</li><li>Contact us</li><li>Privacy policy</li></ul>
    </div>
    <div class="col" style="left:398px">
      <h5>What makes us different</h5><div class="bar"></div>
      <ul class="links"><li>Our Philosophy</li><li>Maren’s Biography</li><li>Clara’s Biography</li><li>Our Associates</li></ul>
    </div>
    <div class="col" style="left:590px">
      <h5>Learn about mediation services</h5><div class="bar"></div>
      <ul class="links"><li>Commercial Meditation</li><li>Conflict Coaching</li><li>Elder &amp; Adult Sibling Meditation</li><li>Meeting or Project Facilitation</li><li style="height:26px">Negotiation</li><li>Divorce &amp; Post-Divorce Meditation</li></ul>
    </div>
    <div class="col" style="left:815px">
      <h5>Conflict consulting</h5><div class="bar"></div>
      <ul class="links"><li>Who Should Work With Us</li><li>Value &amp; Benefits</li><li>Outcomes</li></ul>
    </div>
  </footer>
  <div class="abs copyright">COPYRIGHT © 2014 HMG. ALL RIGHTS RESERVED.</div>

</div>
</body>
</html>
```